Business Card Design

We like to use greens as you will see in our logo (but not TOO much green). We are a Dental Clinic in a somewhat eccentric community. We do not like the dated sharp designs which we see many dentists use. We're looking for something bright and fresh while still maintaining the integrity of the profession. Elegance is not necessarily what we are going for... we need for the design to be "mature" but also up-lifting.

See our logo.
Updates

Project Deadline Extended
Reason: We have 5 designs which we like. But we'd like to see a few more before committing to a design.

Project Deadline Extended
Reason: We are awaiting revisions to this project. We are still welcoming designs while we wait to see if designers are able to provide to us the revisions we require in order to proceed with a selection.

Target Market(s)

Younger families - ages late 20's to early 40's

Industry/Entity Type

Business

Contact Information for Business Card

Marlow T. Venn DDS 2737 S. Fennimore Ave. Ste. 8 Alder Grove, OR 97035 (555)555-0174 FX (555)555-0189 info@BrightwaveDentalMi.example BrigthwaveDentalMi.example on the back of the card we need an appointment reminder (For____ Date___ Time____) with "If you are unable to keep your appointment, kindly give 48 hours notice" at the bottom. No use of teeth in the design. DOUBLE SIDED DESIGN

Requirements
Should not have
• The use of pictures of teeth

```html
<!DOCTYPE html>
<html lang="en">
<head>
<meta charset="utf-8">
<title>Brightwave Dental Care – Business Card</title>
<link rel="stylesheet" href="https://fonts.googleapis.com/css2?family=Source+Sans+3:ital,wght@0,400;0,600;0,700;1,400&family=Cinzel:wght@600&display=swap">
<style>
  :root {
    --green-deep: #17693a;
    --green-bright: #8cc63f;
    --green-soft: #a9d46a;
    --ink: #333333;
    --paper: #ffffff;
    --backdrop: #ecebe8;
    --rule: #8a8a8a;
    --box-line: #555555;
  }
  * { box-sizing: border-box; margin: 0; padding: 0; }
  html, body { width: 1200px; height: 1184px; overflow: hidden; }
  body {
    position: relative;
    background: var(--backdrop);
    font-family: "Source Sans 3", "Myriad Pro", Arial, sans-serif;
    color: var(--ink);
  }
  .card {
    position: absolute;
    background: var(--paper);
    box-shadow: 0 2px 6px rgba(0,0,0,.18);
    overflow: hidden;
  }

  /* ---------- Front ---------- */
  .card-front { left: 27px; top: 27px; width: 938px; height: 537px; }
  .front-band {
    position: absolute; left: 0; top: 0; width: 100%; height: 123px;
    background: var(--green-deep);
  }
  .front-stripe {
    position: absolute; left: 0; top: 129px; width: 100%; height: 8px;
    background: var(--green-bright);
  }
  .brand-dot {
    position: absolute; left: 413px; top: 34px; width: 118px; height: 118px;
    border-radius: 50%; background: var(--green-soft);
    border: 8px solid var(--paper);
  }
  .brand-front {
    position: absolute; left: 0; top: 160px; width: 100%;
    text-align: center; color: var(--green-deep);
    font-weight: 600; line-height: 1;
  }
  .brand-front .brand-main { display: block; font-size: 80px; letter-spacing: -1px; }
  .brand-front .brand-sub { display: block; font-size: 44px; letter-spacing: 3px; margin-top: 8px; margin-left: 6px; }

  .person {
    position: absolute; right: 498px; top: 348px; text-align: right;
    font-size: 24px; line-height: 37px;
  }
  .person-name { color: var(--green-deep); font-weight: 700; font-size: 31px; line-height: 40px; }
  .person-title { margin-bottom: 8px; }
  .divider {
    position: absolute; left: 447px; top: 348px; width: 2px; height: 152px;
    background: var(--rule);
  }
  .contacts {
    position: absolute; left: 461px; top: 346px; list-style: none;
    font-size: 23px; line-height: 41px;
  }
  .contacts li { display: flex; align-items: center; gap: 8px; }
  .contacts svg { width: 17px; height: 17px; fill: var(--ink); flex: none; }

  /* ---------- Back ---------- */
  .card-back { left: 237px; top: 597px; width: 944px; height: 539px; }
  .brand-back {
    position: absolute; left: 76px; top: 26px;
    color: var(--green-deep); font-weight: 600; line-height: 1;
    display: flex; align-items: center; gap: 12px;
  }
  .brand-back .brand-dot-sm {
    width: 48px; height: 48px; border-radius: 50%; background: var(--green-soft); flex: none;
  }
  .brand-back .brand-main { display: block; font-size: 52px; letter-spacing: -1px; }
  .brand-back .brand-sub { display: block; font-size: 28px; letter-spacing: 2px; margin-top: 4px; }

  .appt-title {
    position: absolute; left: 81px; top: 172px;
    font-family: "Cinzel", "Trajan Pro", serif; font-weight: 600;
    font-size: 34px; color: var(--green-deep); letter-spacing: 1px;
  }
  .field-row {
    position: absolute; left: 83px; display: flex; align-items: flex-end;
    font-size: 27px; color: var(--ink);
  }
  .blank {
    display: inline-block; border-bottom: 2px dotted var(--rule);
    height: 1px; margin: 0 4px 9px;
  }
  .row-name { top: 252px; }
  .row-date { top: 318px; }
  .row-next { top: 384px; align-items: center; }
  .next-box {
    display: inline-block; width: 168px; height: 36px;
    border: 2px solid var(--box-line); border-radius: 4px;
  }
  .days {
    position: absolute; right: 28px; top: 76px; list-style: none;
    font-weight: 700; font-size: 28px;
  }
  .days li {
    display: flex; justify-content: flex-end; align-items: center;
    gap: 15px; height: 34px; margin-bottom: 31px;
  }
  .days li .day-box {
    width: 59px; height: 34px; border: 2px solid var(--box-line); border-radius: 4px;
  }
  .days li.day-fri { margin-top: -4px; }
  .notice {
    position: absolute; left: 80px; top: 460px;
    font-style: italic; font-size: 27px; color: var(--ink);
  }
  .back-band {
    position: absolute; left: 0; bottom: 0; width: 100%; height: 14px;
    background: var(--green-deep);
  }
</style>
</head>
<body>

<section class="card card-front" aria-label="Business card front">
  <div class="front-band"></div>
  <div class="front-stripe"></div>
  <div class="brand-dot"></div>
  <div class="brand-front">
    <span class="brand-main">Brightwave</span>
    <span class="brand-sub">DENTAL CARE</span>
  </div>

  <div class="person">
    <div class="person-name">Marlow T. Venn</div>
    <div class="person-title">DDS</div>
    <div>2737 S. Fennimore Ave.</div>
    <div>Ste. 8 Alder Grove, OR 97035</div>
  </div>
  <div class="divider"></div>
  <ul class="contacts">
    <li>
      <svg viewBox="0 0 24 24" aria-hidden="true"><path d="M6.6 10.8a15.1 15.1 0 0 0 6.6 6.6l2.2-2.2c.3-.3.7-.4 1-.2 1.1.4 2.3.6 3.6.6.6 0 1 .4 1 1V20c0 .6-.4 1-1 1A17 17 0 0 1 3 4c0-.6.4-1 1-1h3.5c.6 0 1 .4 1 1 0 1.3.2 2.5.6 3.6.1.3 0 .7-.2 1z"/></svg>
      (555)555-0174
    </li>
    <li>
      <svg viewBox="0 0 24 24" aria-hidden="true"><path d="M6 3h10v5H6zM3 9h18a1 1 0 0 1 1 1v7h-3v4H5v-4H2v-7a1 1 0 0 1 1-1zm4 7v3h10v-3z"/></svg>
      (555)555-0189
    </li>
    <li>
      <svg viewBox="0 0 24 24" aria-hidden="true"><path d="M2 5h20v14H2zm2 2v.4l8 5.2 8-5.2V7zm0 2.8V17h16V9.8l-8 5.2z"/></svg>
      info@BrightwaveDentalMi.example
    </li>
    <li>
      <svg viewBox="0 0 24 24" aria-hidden="true"><path d="M12 2a10 10 0 1 0 0 20 10 10 0 0 0 0-20zm6.9 9h-3a15 15 0 0 0-1.2-6.1A8 8 0 0 1 18.9 11zM12 4.1c.9 1.2 1.8 3.6 1.9 6.9h-3.8c.1-3.3 1-5.7 1.9-6.9zM9.3 4.9A15 15 0 0 0 8.1 11h-3a8 8 0 0 1 4.2-6.1zM5.1 13h3a15 15 0 0 0 1.2 6.1A8 8 0 0 1 5.1 13zm6.9 6.9c-.9-1.2-1.8-3.6-1.9-6.9h3.8c-.1 3.3-1 5.7-1.9 6.9zm2.7-.8a15 15 0 0 0 1.2-6.1h3a8 8 0 0 1-4.2 6.1z"/></svg>
      BrigthwaveDentalMi.example
    </li>
  </ul>
</section>

<section class="card card-back" aria-label="Business card back, appointment reminder">
  <div class="brand-back">
    <div class="brand-dot-sm"></div>
    <div>
      <span class="brand-main">Brightwave</span>
      <span class="brand-sub">DENTAL CARE</span>
    </div>
  </div>

  <h2 class="appt-title">YOUR APPOINTMENT</h2>

  <div class="field-row row-name">Name :<span class="blank" style="width:522px;margin-left:22px"></span></div>
  <div class="field-row row-date">Date :<span class="blank" style="width:168px;margin-left:30px"></span>&nbsp;Time :<span class="blank" style="width:160px"></span>am / pm</div>
  <div class="field-row row-next">Next Appointment<span class="next-box" style="margin-left:18px"></span><span class="next-box" style="margin-left:40px"></span></div>

  <ul class="days">
    <li>MON<span class="day-box"></span></li>
    <li>TUE<span class="day-box"></span></li>
    <li>WED<span class="day-box"></span></li>
    <li>THU<span class="day-box"></span></li>
    <li class="day-fri">FRI<span class="day-box"></span></li>
    <li>SAT<span class="day-box"></span></li>
  </ul>

  <p class="notice">If you are unable to keep your appointment, kindly give 48 hours notice</p>
  <div class="back-band"></div>
</section>

</body>
</html>
```